Wordpress Design - Accounting Practice Startup

We are a relatively new Accounting Firm in Sydney with a primary focus on the Not-For-Profit sector. We need a complete re-design of our wordpress based website: www.tallowmereledger.com.au
We already have a logo design which we would like to keep using. See uploaded files.
We have a simple menu stucture:
- Home
- About Us
- Our Services
- Contact Us
(Suggestions welcome!)
Happy for it to be a single page scrolling website linked via the menu. We would like the "Our Services" page/section to have icons for the following:
- Bookkeeping
- Payroll
- Accounting
- Training
- Consulting
- Projects
We'd like a banner at the top of the page below the menu, and a place for testimonials, possibly integrated into the body or to the side. Images and icons to be included would be great.
Our main aim is to have an elegant and modern website that works well on all devices.
Updates
Industry/Entity Type
Accounting
Colors
Designer to choose colors to be used in the design.
Look and feel
Each slider illustrates characteristics of the customer's brand and the style your logo design should communicate.

```html
<!DOCTYPE html>
<html lang="en">
<head>
<meta charset="utf-8">
<title>Tallowmere Ledger</title>
<link href="https://fonts.googleapis.com/css2?family=Lato:ital,wght@0,400;0,700;0,900;1,400&display=swap" rel="stylesheet">
<style>
:root{
  --green:#43a23a;
  --ink:#333333;
  --text:#444444;
  --muted:#777777;
  --band:#f1f1f1;
  --dark:#3a3a3a;
  --darker:#2b2b2b;
  --field:#f2f2f2;
  --white:#ffffff;
}
*{margin:0;padding:0;box-sizing:border-box}
html,body{width:1200px;height:2632px;overflow:hidden}
body{font-family:'Lato',sans-serif;color:var(--text);background:var(--white);position:relative}
.abs{position:absolute}

/* header */
.site-header{position:absolute;top:0;left:0;width:1200px;height:105px;background:var(--white)}
.brand{left:75px;top:28px;display:flex;align-items:center;gap:12px}
.brand-mark{width:18px;height:18px;background:var(--green)}
.brand-name{font-size:28px;font-weight:400;color:var(--ink);letter-spacing:.5px;line-height:28px}
.main-nav{left:0;top:0;width:1200px;height:105px}
.nav-link{position:absolute;top:48px;font-size:15px;color:var(--ink);text-transform:uppercase;letter-spacing:.3px}
.nav-link.is-active{color:var(--green)}

/* hero */
.hero{position:absolute;top:105px;left:0;width:1200px;height:556px;
  background:linear-gradient(180deg,#b9a58c 0%,#c8b598 38%,#8a8f86 62%,#4e6a76 100%)}
.hero-title{position:absolute;top:180px;width:1200px;text-align:center;font-size:58px;font-weight:900;color:var(--white);letter-spacing:1px;line-height:70px}
.hero-sub{position:absolute;top:250px;width:1200px;text-align:center;font-size:23px;font-weight:700;color:var(--white);line-height:30px}
.btn{position:absolute;display:flex;align-items:center;justify-content:center;background:var(--green);color:var(--white);font-size:17px;font-weight:700;text-transform:uppercase;letter-spacing:.5px}
.hero .btn{left:510px;top:330px;width:180px;height:44px}
.dots{position:absolute;top:509px;left:569px;display:flex;gap:6px}
.dot{width:10px;height:10px;border-radius:50%;background:var(--white)}
.dot.is-active{background:var(--green)}

/* about */
.about{position:absolute;top:661px;left:0;width:1200px;height:439px}
.about-marker{left:75px;top:102px;width:22px;height:22px;background:var(--green)}
.about-heading{left:152px;top:80px;font-size:28px;font-weight:700;color:var(--ink);line-height:32px;text-transform:uppercase}
.about-heading span{color:var(--green);display:block}
.about-copy{left:75px;top:168px;width:510px;font-size:14px;line-height:24.5px;color:var(--text)}
.about-copy p+p{margin-top:8px}
.about-photo{left:614px;top:60px;width:512px;height:326px;background:linear-gradient(135deg,#3b4a5c 0%,#cfd5dc 45%,#eef1f4 70%,#9aa5b1 100%)}

/* services */
.services{position:absolute;top:1100px;left:0;width:1200px;height:349px;background:var(--band);overflow:hidden}
.section-title{position:absolute;width:1200px;text-align:center;font-size:27px;font-weight:700;color:var(--ink);text-transform:uppercase}
.section-title span{color:var(--green)}
.services .section-title{top:44px}
.service-label{position:absolute;font-size:18px;font-weight:700;color:var(--green);text-transform:uppercase;letter-spacing:.3px}
.service-label.left{text-align:right;width:240px}
.arch-name{position:absolute;left:420px;top:252px;width:360px;text-align:center;font-size:30px;font-weight:400;color:var(--ink);line-height:1.1}

/* testimonials */
.testimonials{position:absolute;top:1449px;left:0;width:1200px;height:461px}
.testimonials .section-title{top:52px}
.quote-card{position:absolute;top:119px;width:330px;height:202px;border:2px solid #d4d4d4;padding:22px 20px;text-align:center;font-size:14px;font-style:italic;line-height:27px;color:var(--muted)}
.avatar{position:absolute;top:290px;width:62px;height:62px;border-radius:50%;border:3px solid #e4e4e4;background:linear-gradient(180deg,#d9d9d9,#9a9a9a)}
.person-name{position:absolute;top:364px;width:330px;text-align:center;font-size:15px;font-weight:700;color:var(--green);text-transform:uppercase}
.person-loc{position:absolute;top:390px;width:330px;text-align:center;font-size:12px;font-style:italic;color:var(--muted)}

/* contact */
.contact{position:absolute;top:1910px;left:0;width:1200px;height:654px;background:var(--dark)}
.contact .section-title{top:44px;color:var(--white)}
.consultant{position:absolute;top:106px;width:320px;color:var(--white)}
.consultant-icon{position:absolute;left:0;top:0;width:44px;height:44px;border-radius:50%;border:2px solid var(--white);display:flex;align-items:center;justify-content:center}
.consultant-name{position:absolute;top:0;font-size:21px;font-weight:700;color:var(--green)}
.consultant-role{position:absolute;top:29px;font-size:14px;font-weight:700}
.consultant-line{position:absolute;font-size:14px;display:flex;align-items:center;gap:16px}
.quick-title{position:absolute;top:262px;width:1200px;text-align:center;font-size:21px;font-weight:700;color:var(--white);text-transform:uppercase}
.quick-title span{color:var(--green)}
.field{position:absolute;background:var(--field);font-size:13px;color:var(--ink);padding:0 18px;display:flex;align-items:center}
.field.message{align-items:flex-start;padding-top:16px}
.contact .btn{left:510px;top:544px;width:180px;height:47px}

/* footer */
.site-footer{position:absolute;top:2564px;left:0;width:1200px;height:68px;background:var(--darker)}
.copyright{position:absolute;left:75px;top:26px;font-size:13px;color:#8a8a8a}
.social{position:absolute;right:70px;top:22px;display:flex;gap:18px}
.social-dot{width:22px;height:22px;border-radius:50%;background:#d8d8d8}
</style>
</head>
<body>

<header class="site-header">
  <div class="abs brand"><span class="brand-mark"></span><span class="brand-name">TALLOWMERE<br>LEDGER</span></div>
  <nav class="abs main-nav">
    <span class="nav-link is-active" style="left:643px">Home</span>
    <span class="nav-link" style="left:742px">About Us</span>
    <span class="nav-link" style="left:872px">Our Services</span>
    <span class="nav-link" style="left:1030px">Contact Us</span>
  </nav>
</header>

<section class="hero" role="img" aria-label="Harbour view of the Sydney waterfront and city skyline at sunset">
  <h1 class="hero-title">TALLOWMERE LEDGER</h1>
  <p class="hero-sub">We are a new Accounting Firm in Sydney with a primary focus<br>on the Not-For-Profit sector.</p>
  <span class="btn">Read More</span>
  <div class="dots"><span class="dot is-active"></span><span class="dot"></span><span class="dot"></span><span class="dot"></span></div>
</section>

<section class="about">
  <span class="abs about-marker"></span>
  <h2 class="abs about-heading">About<span>Tallowmere Ledger</span></h2>
  <div class="abs about-copy">
    <p>At Tallowmere Ledger, we believe that every number counts. We strive to deliver a premium service at a reasonable cost. Our focus is to ensure your financial needs are met with the quality, integrity, diligence and timeliness that you would expect.<br>Let Tallowmere Ledger help you sort out your finances.</p>
    <p>Tallowmere Ledger originated with the idea of providing accounting services that would make clients feel safe and find refuge, feel confident that they could trust the numbers in their financial reports.</p>
  </div>
  <div class="abs about-photo" role="img" aria-label="Hands working at a desk with a laptop, calculator, phone and printed reports"></div>
</section>

<section class="services">
  <h2 class="section-title">Our <span>Services</span></h2>
  <svg class="abs" style="left:0;top:0" width="1200" height="349" viewBox="0 0 1200 349">
    <g stroke="var(--green)" stroke-width="2.5" fill="none">
      <path d="M394 349 C394 150 806 150 806 349" fill="#ffffff"/>
      <line x1="420" y1="110" x2="462" y2="170"/>
      <line x1="360" y1="190" x2="410" y2="240"/>
      <line x1="360" y1="263" x2="398" y2="295"/>
      <line x1="780" y1="110" x2="738" y2="170"/>
      <line x1="840" y1="190" x2="790" y2="240"/>
      <line x1="840" y1="263" x2="802" y2="295"/>
    </g>
    <g fill="#2f2f2f" stroke="var(--green)" stroke-width="3">
      <circle cx="396" cy="89" r="38"/><circle cx="335" cy="166" r="38"/><circle cx="326" cy="263" r="38"/>
      <circle cx="805" cy="89" r="38"/><circle cx="863" cy="166" r="38"/><circle cx="872" cy="263" r="38"/>
    </g>
    <g fill="none" stroke="#ffffff" stroke-width="3" stroke-linejoin="round">
      <path d="M384 74h22a4 4 0 0 1 4 4v26h-22a4 4 0 0 1-4-4z"/><path d="M384 100a4 4 0 0 1 4-4h22"/>
      <path d="M343 152c-4-4-18-4-18 5s18 5 18 14-14 9-18 4M334 144v44"/>
      <rect x="312" y="247" width="28" height="32" rx="2"/><line x1="316" y1="257" x2="336" y2="257"/>
      <path d="M318 264h2M326 264h2M334 264h2M318 271h2M326 271h2M334 271h2" stroke-width="4"/>
      <rect x="792" y="77" width="26" height="18" rx="1"/><line x1="786" y1="100" x2="824" y2="100"/>
      <path d="M849 156h22a3 3 0 0 1 3 3v10a3 3 0 0 1-3 3h-12l-7 6v-6h-3a3 3 0 0 1-3-3v-10a3 3 0 0 1 3-3z" fill="#ffffff"/>
      <path d="M862 248h14l7 7v24h-21z" fill="#ffffff"/>
    </g>
    <g stroke="#2f2f2f" stroke-width="2"><line x1="866" y1="262" x2="878" y2="262"/><line x1="866" y1="268" x2="878" y2="268"/><line x1="866" y1="274" x2="874" y2="274"/></g>
  </svg>
  <span class="service-label left" style="left:86px;top:78px">Bookkeeping</span>
  <span class="service-label left" style="left:34px;top:155px">Payroll</span>
  <span class="service-label left" style="left:18px;top:252px">Accounting</span>
  <span class="service-label" style="left:872px;top:78px">Training</span>
  <span class="service-label" style="left:928px;top:155px">Consulting</span>
  <span class="service-label" style="left:940px;top:252px">Projects</span>
  <div class="arch-name">TALLOWMERE<br>LEDGER</div>
</section>

<section class="testimonials">
  <h2 class="section-title">Our <span>Testimonials</span></h2>
  <blockquote class="quote-card" style="left:75px">“ Vestibulum ante ipsum primis in faucibus orci luctus et ultrices posuere cubilia aliquam nibh a dui iaculis viverra id a velit. Vivamus egestas risus in magna varius commodo primis sed semper viverra egestas..”</blockquote>
  <blockquote class="quote-card" style="left:435px">“ Vestibulum ante ipsum primis in faucibus orci luctus et ultrices posuere cubilia aliquam nibh a dui iaculis viverra id a velit. Vivamus egestas risus in magna varius commodo primis sed semper viverra egestas..”</blockquote>
  <blockquote class="quote-card" style="left:796px">“ Vestibulum ante ipsum primis in faucibus orci luctus et ultrices posuere cubilia aliquam nibh a dui iaculis viverra id a velit. Vivamus egestas risus in magna varius commodo primis sed semper viverra egestas..”</blockquote>
  <div class="avatar" style="left:209px" role="img" aria-label="Client portrait"></div>
  <div class="avatar" style="left:569px" role="img" aria-label="Client portrait"></div>
  <div class="avatar" style="left:930px" role="img" aria-label="Client portrait"></div>
  <div class="person-name" style="left:75px">Name Heading</div><div class="person-loc" style="left:75px">Location</div>
  <div class="person-name" style="left:435px">Name Heading</div><div class="person-loc" style="left:435px">Location</div>
  <div class="person-name" style="left:796px">Name Heading</div><div class="person-loc" style="left:796px">Location</div>
</section>

<section class="contact">
  <h2 class="section-title">Contact <span>Us</span></h2>

  <div class="consultant" style="left:255px">
    <span class="consultant-icon"><svg width="20" height="22" viewBox="0 0 20 22"><circle cx="10" cy="6" r="5" fill="#fff"/><path d="M0 22c0-7 4-10 10-10s10 3 10 10z" fill="#fff"/></svg></span>
    <span class="consultant-name" style="left:62px">Mira Okafor</span>
    <span class="consultant-role" style="left:62px">Principal Consultant</span>
    <span class="consultant-line" style="left:62px;top:64px"><svg width="14" height="10" viewBox="0 0 14 10"><rect width="14" height="10" fill="#fff"/><path d="M0 0l7 6 7-6" stroke="#3a3a3a" fill="none" stroke-width="1.5"/></svg>mira@tallowmereledger.com.au</span>
    <span class="consultant-line" style="left:62px;top:96px"><svg width="12" height="12" viewBox="0 0 12 12"><path d="M2 0l3 3-2 2c1 2 2 3 4 4l2-2 3 3-2 2C5 12 0 7 0 2z" fill="#fff"/></svg>0400 118 320</span>
  </div>

  <div class="consultant" style="left:614px">
    <span class="consultant-icon"><svg width="20" height="22" viewBox="0 0 20 22"><circle cx="10" cy="6" r="5" fill="#fff"/><path d="M0 22c0-7 4-10 10-10s10 3 10 10z" fill="#fff"/></svg></span>
    <span class="consultant-name" style="left:61px">Daniel Brisk</span>
    <span class="consultant-role" style="left:61px">Consultant</span>
    <span class="consultant-line" style="left:61px;top:64px"><svg width="14" height="10" viewBox="0 0 14 10"><rect width="14" height="10" fill="#fff"/><path d="M0 0l7 6 7-6" stroke="#3a3a3a" fill="none" stroke-width="1.5"/></svg>daniel@tallowmereledger.com.au</span>
    <span class="consultant-line" style="left:61px;top:96px"><svg width="12" height="12" viewBox="0 0 12 12"><path d="M2 0l3 3-2 2c1 2 2 3 4 4l2-2 3 3-2 2C5 12 0 7 0 2z" fill="#fff"/></svg>0400 227 491</span>
  </div>

  <h3 class="quick-title">Quick <span>Contact</span></h3>
  <div class="field" style="left:254px;top:312px;width:334px;height:48px">Enter Name</div>
  <div class="field" style="left:614px;top:312px;width:333px;height:48px">Phone No</div>
  <div class="field" style="left:254px;top:372px;width:334px;height:49px">Email Address</div>
  <div class="field" style="left:614px;top:372px;width:333px;height:49px;justify-content:space-between">Subject<svg width="10" height="6" viewBox="0 0 10 6"><path d="M1 1l4 4 4-4" stroke="#555" fill="none" stroke-width="1.3"/></svg></div>
  <div class="field message" style="left:254px;top:432px;width:693px;height:87px">Message</div>
  <span class="btn">Submit</span>
</section>

<footer class="site-footer">
  <p class="copyright">Copyright © 2017. Company Name All Right Reserved</p>
  <div class="social"><span class="social-dot"></span><span class="social-dot"></span><span class="social-dot"></span><span class="social-dot"></span><span class="social-dot"></span></div>
</footer>

</body>
</html>
```